Birchline Septic Solutions

Would like to see some single sided ones but would also like to see some double sided with one sided only being the logo. Owners name is Tom Halvick. Phone number is 555-214-0387
Services are pumping, inspections, installs, and repairs

Contact Information for Business Card

555-241-0387 Tom Halvick Greenfield, OH

```html
<!DOCTYPE html>
<html lang="en">
<head>
<meta charset="utf-8">
<title>Birchline Septic Solutions – Business Cards</title>
<link rel="stylesheet" href="https://fonts.googleapis.com/css2?family=Montserrat:wght@400;500;600;700;800&display=swap">
<style>
  :root {
    --backdrop: #5fb8b4;
    --accent: #5ab8b4;
    --card-light: #ffffff;
    --card-dark: #000000;
    --ink: #111111;
    --ink-inverse: #ffffff;
    --text-muted: #555555;
    --divider: #e6e6e6;
  }
  html, body {
    margin: 0;
    padding: 0;
    width: 1200px;
    height: 1200px;
    overflow: hidden;
    background: var(--backdrop);
    font-family: "Montserrat", sans-serif;
  }
  .canvas {
    position: relative;
    width: 1200px;
    height: 1200px;
  }
  .card {
    position: absolute;
    left: 147px;
    width: 908px;
    height: 520px;
    border-radius: 43px;
    overflow: hidden;
  }
  .card--front { top: 55px; background: var(--card-light); }
  .card--back { top: 624px; background: var(--card-dark); }

  .brand {
    position: absolute;
    display: flex;
    flex-direction: column;
    align-items: center;
    font-weight: 800;
    text-transform: uppercase;
    line-height: 1;
  }
  .brand__name { letter-spacing: 1px; }
  .brand__tagline { letter-spacing: 5px; margin-top: 12px; }

  .card--front .brand {
    left: 108px;
    top: 230px;
    width: 212px;
    color: var(--ink);
  }
  .card--front .brand__name { font-size: 38px; }
  .card--front .brand__tagline { font-size: 13px; letter-spacing: 4px; }

  .card--back .brand {
    left: 0;
    right: 0;
    top: 218px;
    color: var(--ink-inverse);
  }
  .card--back .brand__name { font-size: 56px; }
  .card--back .brand__tagline { font-size: 19px; letter-spacing: 6px; margin-top: 16px; }

  .divider {
    position: absolute;
    left: 415px;
    top: 208px;
    width: 2px;
    height: 156px;
    background: var(--divider);
  }

  .contact {
    position: absolute;
    left: 518px;
    top: 178px;
  }
  .contact__name {
    margin: 0 0 24px;
    font-size: 42px;
    font-weight: 700;
    color: var(--accent);
    line-height: 1;
  }
  .contact__list {
    list-style: none;
    margin: 0;
    padding: 0;
  }
  .contact__item {
    display: flex;
    align-items: center;
    height: 26px;
    margin-bottom: 27px;
    font-size: 21px;
    font-weight: 500;
    color: var(--text-muted);
  }
  .contact__item:nth-child(3) { margin-top: -1px; }
  .contact__icon {
    width: 24px;
    height: 24px;
    margin-right: 35px;
    flex: none;
  }
</style>
</head>
<body>
<main class="canvas">

  <section class="card card--front" aria-label="Business card front">
    <div class="brand">
      <span class="brand__name">Birchline</span>
      <span class="brand__tagline">Septic Solutions</span>
    </div>

    <div class="divider"></div>

    <div class="contact">
      <h1 class="contact__name">Tom Halvick</h1>
      <ul class="contact__list">
        <li class="contact__item">
          <svg class="contact__icon" viewBox="0 0 24 24" aria-hidden="true">
            <path fill="var(--accent)" d="M6.6 10.8a15.1 15.1 0 0 0 6.6 6.6l2.2-2.2a1 1 0 0 1 1-.25 11.4 11.4 0 0 0 3.6.57 1 1 0 0 1 1 1V20a1 1 0 0 1-1 1A17 17 0 0 1 3 4a1 1 0 0 1 1-1h3.5a1 1 0 0 1 1 1c0 1.25.2 2.45.57 3.57a1 1 0 0 1-.25 1z"/>
          </svg>
          555-214-0387
        </li>
        <li class="contact__item">
          <svg class="contact__icon" viewBox="0 0 24 24" aria-hidden="true">
            <path fill="none" stroke="var(--accent)" stroke-width="2" stroke-linecap="round" d="M16 12a4 4 0 1 1-4-4 4 4 0 0 1 4 4v1.5a2.5 2.5 0 0 0 5 0V12a9 9 0 1 0-3.5 7.1"/>
          </svg>
          email@website.com
        </li>
        <li class="contact__item">
          <svg class="contact__icon" viewBox="0 0 24 24" aria-hidden="true">
            <circle cx="12" cy="12" r="11" fill="var(--accent)"/>
            <g fill="none" stroke="#ffffff" stroke-width="1.4">
              <ellipse cx="12" cy="12" rx="4.5" ry="11"/>
              <line x1="12" y1="1" x2="12" y2="23"/>
              <line x1="1" y1="12" x2="23" y2="12"/>
            </g>
          </svg>
          www.website.com
        </li>
      </ul>
    </div>
  </section>

  <section class="card card--back" aria-label="Business card back">
    <div class="brand">
      <span class="brand__name">Birchline</span>
      <span class="brand__tagline">Septic Solutions</span>
    </div>
  </section>

</main>
</body>
</html>
```